Visitenkarten für Kfz Sachverständigenbüro - Ingenieurbüro Wolkenmeier
Zielgruppe
Erstellung von Unfallgutachten, Oldtimergutachten, Fahrzeugbewertungen, technischen Gutachten etc.
Zielgruppen: Autohäuser, Werkstätten, Oldtimerliebhaber, Privatkunden mit Unfallschäden
Aufgabenstellung
Möglichst beidseitige Visitenkarten mit Firmenlogo integriert, "Firmenfarbe" blau
Ursprüngliche Visitenkarten mit Logo im Anhang

```html
<!DOCTYPE html>
<html lang="de">
<head>
<meta charset="utf-8">
<title>Visitenkarten – Ingenieurbüro Wolkenmeier</title>
<link rel="stylesheet" href="https://fonts.googleapis.com/css2?family=Arimo:wght@400;700&display=swap">
<style>
  :root {
    --brand-blue: #1a1aff;
    --band-light: rgba(164, 164, 255, 0.55);
    --band-dark: rgba(77, 77, 255, 0.45);
    --ink: #000000;
    --paper: #ffffff;
    --card-edge: #8a8a8a;
    --page: #ffffff;
  }
  html, body {
    margin: 0;
    width: 1200px;
    height: 510px;
    overflow: hidden;
    background: var(--page);
    font-family: "Arimo", Arial, sans-serif;
  }
  .sheet { position: relative; width: 1200px; height: 510px; }
  .card {
    position: absolute;
    top: 85px;
    width: 501px;
    height: 324px;
    background: var(--paper);
    border: 1px solid var(--card-edge);
    box-sizing: border-box;
    overflow: hidden;
  }
  .card--front { left: 64px; }
  .card--back { left: 631px; }

  /* Front: company name mark */
  .front-mark {
    position: absolute;
    left: 0; right: 0; top: 118px;
    text-align: center;
    color: var(--brand-blue);
  }
  .front-mark__name {
    display: inline-flex;
    align-items: center;
    gap: 12px;
    font-size: 31px;
    font-weight: 400;
  }
  .front-mark__dot {
    width: 16px; height: 16px;
    border-radius: 50%;
    background: var(--brand-blue);
  }
  .front-mark__tagline {
    margin-top: 14px;
    font-size: 19px;
    letter-spacing: 1.5px;
  }

  /* Back */
  .back-decor {
    position: absolute;
    left: 330px; top: 0;
    width: 171px; height: 240px;
    background: radial-gradient(ellipse at 100% 0%, var(--band-dark) 0%, var(--band-light) 45%, rgba(255,255,255,0) 80%);
  }
  .back-text {
    position: absolute;
    left: 0; width: 500px;
    text-align: center;
    color: var(--ink);
    font-weight: 700;
  }
  .person { top: 38px; font-size: 19px; font-weight: 400; -webkit-text-stroke: 0.4px var(--ink); }
  .role { top: 70px; font-size: 15px; }
  .address { top: 118px; font-size: 15px; line-height: 19px; }
  .online { top: 175px; font-size: 15px; line-height: 18px; }
  .phones {
    position: absolute;
    right: 36px; top: 245px;
    text-align: right;
    font-size: 16px;
    font-weight: 700;
    line-height: 20px;
    color: var(--ink);
  }
  .back-mark {
    position: absolute;
    left: 160px; top: 262px;
    display: flex;
    align-items: center;
    gap: 6px;
    color: var(--brand-blue);
    font-size: 13px;
    font-weight: 400;
  }
  .back-mark__square { width: 9px; height: 9px; background: var(--brand-blue); }
</style>
</head>
<body>
<main class="sheet">
  <section class="card card--front" aria-label="Vorderseite">
    <div class="front-mark">
      <div class="front-mark__name"><span class="front-mark__dot"></span>Ingenieurbüro Wolkenmeier</div>
      <div class="front-mark__tagline">KFZ-Sachverständige</div>
    </div>
  </section>

  <section class="card card--back" aria-label="Rückseite">
    <div class="back-decor" role="img" aria-label="Dekorative blaue Bögen in der oberen rechten Ecke"></div>
    <div class="back-text person">Dipl.-Ing.(FH) Max Wolkenmeier</div>
    <div class="back-text role">KFZ-Sachverständiger</div>
    <div class="back-text address">Birkenstraße 14<br>65812 Bad Soden</div>
    <div class="back-text online">maxw@ingbuero-wolkenmeier.de<br>www.ingbuero-wolkenmeier.de</div>
    <div class="phones">
      M: 0170-482 9137<br>
      T: 06192-5184 und 5186<br>
      F: 06192-73402
    </div>
    <div class="back-mark"><span class="back-mark__square"></span>Wolkenmeier</div>
  </section>
</main>
</body>
</html>
```